Company Stationary

I'd like a template to use for company stationery. We frequently write short 1 - 2 page Word documents (which we save as PDF) to clients and prospects and the presentation is boring and doesn't look professional. I am looking for a Word template that will convey a better sense of professionalism. The design should include our logo (attached) but be simple and elegant. It should save nicely as a PDF, since that is how we will send the files via email.

Target Market(s)

Financial Institutions

Industry/Entity Type

Financial Service

Font styles to use
Serif

Colors

Designer to choose colors to be used in the design.

Requirements
Must have
• Simple design. Needs to be subtle. I don't want the design to be more interesting than the message we are writing.
Nice to have
• When the reader sees it, I want them to feel they are reading something published by a large, very successful company.
Should not have
• Not overpowering design and colors.

```html
<!DOCTYPE html>
<html lang="en">
<head>
<meta charset="utf-8">
<title>Meridal Company Stationery</title>
<link rel="stylesheet" href="https://fonts.googleapis.com/css2?family=Open+Sans:wght@400;600;700&display=swap">
<style>
  :root {
    --ink: #111111;
    --red: #e2231a;
    --paper: #ffffff;
    --backdrop: #e9e8e4;
    --muted: #333333;
    --window: #e4e4e4;
    --rule: #b9b9b9;
    --shadow: 0 6px 14px rgba(0,0,0,0.22);
  }
  * { box-sizing: border-box; margin: 0; padding: 0; }
  html, body { width: 1200px; height: 1024px; overflow: hidden; }
  body {
    background: var(--backdrop);
    font-family: "Open Sans", Arial, sans-serif;
    color: var(--ink);
    position: relative;
  }
  .piece { position: absolute; background: var(--paper); box-shadow: var(--shadow); overflow: hidden; }

  /* Footer band: straight black block under a thin red rule */
  .band { position: absolute; left: 0; right: 0; bottom: 0; background: var(--ink); }
  .band::before { content: ""; position: absolute; left: 0; right: 0; top: -7px; height: 3px; background: var(--red); }

  .brand { font-weight: 700; color: var(--ink); letter-spacing: -0.02em; white-space: nowrap; display: inline-flex; align-items: center; line-height: 1; }
  .brand::after { content: ""; display: inline-block; width: 0.28em; height: 0.28em; background: var(--red); margin-left: 0.14em; align-self: flex-end; margin-bottom: 0.12em; }
  .brand.on-dark { color: var(--paper); }

  .contact { list-style: none; }
  .contact li { display: flex; align-items: center; gap: 4px; white-space: nowrap; }
  .icon { width: 1.2em; height: 1.2em; fill: var(--red); flex: none; }

  /* Letterhead */
  .letterhead { left: 26px; top: 48px; width: 357px; height: 539px; }
  .letterhead .brand { position: absolute; left: 30px; top: 40px; font-size: 20px; }
  .letterhead .address { position: absolute; left: 184px; top: 30px; font-size: 6.5px; line-height: 1.35; text-align: right; width: 76px; }
  .letterhead .divider { position: absolute; left: 266px; top: 30px; width: 1px; height: 28px; background: #999; }
  .letterhead .contact { position: absolute; left: 272px; top: 30px; font-size: 6.3px; line-height: 1.35; }
  .letter-body { position: absolute; left: 30px; top: 110px; width: 306px; font-size: 6.4px; line-height: 1.45; text-align: justify; color: var(--muted); }
  .letter-body p { margin-bottom: 8px; }
  .letter-body .date, .letter-body .greeting { margin-bottom: 4px; text-align: left; }
  .signature { position: absolute; left: 30px; top: 372px; width: 100px; height: 18px; background: linear-gradient(90deg, #d8d8d8, #eeeeee); border-radius: 2px; }
  .signatory { position: absolute; left: 30px; top: 394px; font-size: 6.5px; }
  .letterhead .band { height: 18px; }

  /* Folder */
  .folder { left: 402px; top: 48px; width: 413px; height: 581px; }
  .folder .band { height: 360px; }
  .folder .band::before { top: -14px; height: 8px; }
  .folder .brand { position: absolute; left: 66px; top: 82px; font-size: 48px; }
  .folder .web { position: absolute; left: 0; right: 0; bottom: 22px; text-align: center; color: var(--paper); font-size: 11px; z-index: 1; }

  /* Notepad */
  .notepad { left: 836px; top: 101px; width: 334px; height: 469px; }
  .notepad .brand { position: absolute; left: 106px; top: 38px; font-size: 20px; }
  .ruled { position: absolute; left: 24px; top: 88px; width: 286px; height: 264px;
    background: repeating-linear-gradient(to bottom, transparent 0 16px, var(--rule) 16px 17px); }
  .notepad .contact { position: absolute; left: 24px; top: 396px; font-size: 6px; line-height: 1.4; }
  .notepad .band { height: 18px; }

  /* Business card front */
  .card-front { left: 46px; top: 612px; width: 325px; height: 186px; }
  .card-front .brand { position: absolute; left: 24px; top: 30px; font-size: 24px; }
  .card-front .name { position: absolute; left: 24px; top: 76px; font-size: 12px; font-weight: 600; color: var(--red); }
  .card-front .role { position: absolute; left: 24px; top: 92px; font-size: 8px; font-weight: 700; }
  .card-front .address { position: absolute; left: 24px; top: 112px; font-size: 9px; line-height: 1.3; }
  .card-front .contact { position: absolute; left: 168px; top: 97px; font-size: 9px; line-height: 1.35; }
  .card-front .band { height: 18px; }

  /* Business card back */
  .card-back { left: 46px; top: 822px; width: 328px; height: 186px; background: var(--ink); }
  .card-back .brand { position: absolute; left: 0; right: 0; top: 70px; justify-content: center; font-size: 28px; }
  .card-back .web { position: absolute; left: 0; right: 0; bottom: 22px; text-align: center; color: var(--paper); font-size: 8px; }

  /* Envelope back */
  .envelope-back { left: 608px; top: 754px; width: 542px; height: 235px; }
  .envelope-back .flap { position: absolute; left: 0; top: 0; width: 100%; height: 36px; background: var(--ink); }

  /* Envelope front */
  .envelope-front { left: 402px; top: 658px; width: 538px; height: 231px; }
  .envelope-front .brand { position: absolute; left: 34px; top: 40px; font-size: 26px; }
  .envelope-front .address { position: absolute; left: 38px; top: 96px; font-size: 7.5px; }
  .window { position: absolute; left: 34px; top: 112px; width: 197px; height: 48px; border-radius: 8px; border: 1px solid #bdbdbd; background: linear-gradient(180deg, #f4f4f4, var(--window)); }
  .envelope-front .contact { position: absolute; left: 398px; top: 38px; font-size: 8px; line-height: 1.35; }
  .envelope-front .band { height: 22px; }
</style>
</head>
<body>

<svg width="0" height="0" style="position:absolute" aria-hidden="true">
  <defs>
    <symbol id="i-phone" viewBox="0 0 10 10"><rect x="1" y="3" width="8" height="6" rx="1"/><rect x="0" y="1" width="10" height="2.4" rx="1"/></symbol>
    <symbol id="i-mail" viewBox="0 0 10 10"><path d="M0 2h10v6H0z M0.8 2.6 5 5.6 9.2 2.6" stroke="#fff" stroke-width="0.8"/></symbol>
    <symbol id="i-web" viewBox="0 0 10 10"><circle cx="5" cy="5" r="4.6"/><path d="M0.6 5h8.8M5 0.5v9" stroke="#fff" stroke-width="0.7"/></symbol>
  </defs>
</svg>

<!-- Letterhead -->
<section class="piece letterhead">
  <div class="brand">Meridal</div>
  <div class="address">1204/48 Harbour Lane<br>Sydney NSW 2000<br>Australia</div>
  <div class="divider"></div>
  <ul class="contact">
    <li><svg class="icon"><use href="#i-phone"/></svg>+61(0)4012 345 678</li>
    <li><svg class="icon"><use href="#i-mail"/></svg>daniel@meridal.com</li>
    <li><svg class="icon"><use href="#i-web"/></svg>www.meridal.com</li>
  </ul>
  <div class="letter-body">
    <p class="date">October/09/2017</p>
    <p class="greeting">Dear Michael,</p>
    <p>Thank you for taking the time to meet with our team last week. As discussed, we have prepared a summary of the proposed arrangements for your review, covering the timeline, the responsibilities of each party and the reporting schedule we intend to follow. We believe this approach will give your organisation a clear view of progress at every stage while keeping the administrative burden on your staff to a minimum.</p>
    <p>Our firm has worked alongside financial institutions for many years, and we understand the importance of accuracy, discretion and timely communication. Each engagement is led by a senior adviser who remains your single point of contact from the first meeting through to final delivery. Supporting documents, including the detailed scope of work and the fee schedule, are enclosed with this letter. Should any item require clarification, or should your circumstances change before the agreement is signed, please let us know and we will gladly revise the proposal to reflect your needs. We look forward to your feedback on the enclosed material.</p>
    <p>A short overview of the key dates is set out below so that your team can plan resources and approvals well in advance of the first review meeting.</p>
    <p>We are confident that this partnership will deliver lasting value for your organisation. Our reporting will be concise and consistent, with each update highlighting the decisions required, the risks identified and the actions already taken. If you would prefer a different format or a more frequent schedule, we are happy to adjust our process accordingly. Thank you once again for your trust in our team. We look forward to working with you and to building a strong and productive relationship over the coming years.</p>
  </div>
  <div class="signature" role="img" aria-label="Handwritten signature of Daniel Hart"></div>
  <div class="signatory">Company Director</div>
  <div class="band"></div>
</section>

<!-- Presentation folder -->
<section class="piece folder">
  <div class="brand">Meridal</div>
  <div class="band"></div>
  <div class="web">www.meridal.com</div>
</section>

<!-- Notepad -->
<section class="piece notepad">
  <div class="brand">Meridal</div>
  <div class="ruled"></div>
  <ul class="contact">
    <li><svg class="icon"><use href="#i-phone"/></svg>+61(0)4012 345 678</li>
    <li><svg class="icon"><use href="#i-mail"/></svg>daniel@meridal.com</li>
    <li><svg class="icon"><use href="#i-web"/></svg>www.meridal.com</li>
  </ul>
  <div class="band"></div>
</section>

<!-- Business card, front -->
<section class="piece card-front">
  <div class="brand">Meridal</div>
  <div class="name">DANIEL HART</div>
  <div class="role">JOB TITLE</div>
  <div class="address">1204/48 Harbour Lane<br>Sydney NSW 2000<br>Australia</div>
  <ul class="contact">
    <li><svg class="icon"><use href="#i-phone"/></svg>+61(0)4012 345 678</li>
    <li><svg class="icon"><use href="#i-mail"/></svg>daniel@meridal.com</li>
    <li><svg class="icon"><use href="#i-web"/></svg>www.meridal.com</li>
  </ul>
  <div class="band"></div>
</section>

<!-- Business card, back -->
<section class="piece card-back">
  <div class="brand on-dark">Meridal</div>
  <div class="web">www.meridal.com</div>
</section>

<!-- Envelope, back -->
<section class="piece envelope-back">
  <div class="flap"></div>
</section>

<!-- Envelope, front -->
<section class="piece envelope-front">
  <div class="brand">Meridal</div>
  <div class="address">1204/48 Harbour Lane, Sydney NSW 2000, Australia</div>
  <div class="window"></div>
  <ul class="contact">
    <li><svg class="icon"><use href="#i-phone"/></svg>+61(0)4012 345 678</li>
    <li><svg class="icon"><use href="#i-mail"/></svg>daniel@meridal.com</li>
    <li><svg class="icon"><use href="#i-web"/></svg>www.meridal.com</li>
  </ul>
  <div class="band"></div>
</section>

</body>
</html>
```